Meadowlark Learning Growth Partners (MLGP)

This is a professional business card. Logo and picture are a must on the front of the card. I am an educational consultant. I have been consulting for the past three years for a company. I am now opening my own company. My goal for my consulting company is to eventually consult all over America.

Target Market(s)

Educators, schools, professionals

Industry/Entity Type

Consulting

Contact Information for Business Card

Picture/logo on front, simple modern design

Font styles to use
Serif

Colors
85abd2
0355a3
3176b5
cedeed

Requirements
Must have
• picture, logo,
• Odessa Pruitt, Ed.S
• address 5073 Cormorant ridge Dr. Nashville, TN 37940
• Cell:616-555-0148
• Office: 629-555-0172
• www.Mlgpedu.example
• pruittodessa@mailbox.example

```html
<!DOCTYPE html>
<html lang="en">
<head>
<meta charset="utf-8">
<title>Meadowlark Learning Growth Partners — Business Card</title>
<link rel="stylesheet" href="https://fonts.googleapis.com/css2?family=Work+Sans:wght@400;500;600;700&family=Comfortaa:wght@700&display=swap">
<style>
  :root {
    --navy: #0a3d86;
    --navy-deep: #062c66;
    --brand-blue: #0355a3;
    --mid-blue: #3176b5;
    --sky: #85abd2;
    --mist: #cedeed;
    --paper: #ffffff;
    --paper-shade: #e6e7ea;
    --ink-grey: #4a4f57;
    --stage: #d9dce1;
  }
  * { margin: 0; padding: 0; box-sizing: border-box; }
  html, body { width: 1200px; height: 900px; overflow: hidden; }
  body {
    background: var(--stage);
    font-family: "Work Sans", Arial, sans-serif;
    position: relative;
  }
  .card {
    position: absolute;
    left: 250px;
    width: 700px;
    height: 400px;
    border-radius: 22px;
    overflow: hidden;
    box-shadow: 0 10px 28px rgba(0,0,0,0.22);
  }

  /* Front */
  .card-front {
    top: 30px;
    background: linear-gradient(135deg, var(--paper-shade) 0%, var(--paper) 45%, var(--paper) 70%, var(--paper-shade) 100%);
  }
  .portrait {
    position: absolute;
    left: 92px;
    top: 62px;
    width: 200px;
    height: 200px;
    border-radius: 50%;
    border: 4px solid var(--navy);
    background: radial-gradient(circle at 50% 40%, var(--sky) 0%, var(--mid-blue) 55%, var(--brand-blue) 100%);
  }
  .divider {
    position: absolute;
    left: 336px;
    top: 70px;
    width: 2px;
    height: 200px;
    background: var(--navy);
  }
  .identity {
    position: absolute;
    left: 372px;
    top: 92px;
  }
  .person-name {
    color: var(--navy);
    font-size: 30px;
    font-weight: 600;
    letter-spacing: 0.2px;
  }
  .person-role {
    color: var(--ink-grey);
    font-size: 17px;
    margin-top: 4px;
  }
  .contact-list {
    list-style: none;
    margin-top: 22px;
  }
  .contact-list li {
    display: flex;
    align-items: center;
    gap: 10px;
    color: var(--ink-grey);
    font-size: 17px;
    line-height: 27px;
  }
  .contact-list svg { width: 14px; height: 14px; flex: none; }
  .address-band {
    position: absolute;
    left: 0;
    bottom: 0;
    width: 100%;
    height: 46px;
    background: linear-gradient(90deg, var(--navy-deep), var(--brand-blue));
    color: var(--paper);
    font-size: 16px;
    letter-spacing: 0.3px;
    display: flex;
    align-items: center;
    padding-left: 60px;
  }

  /* Back */
  .card-back {
    top: 470px;
    background: radial-gradient(circle at 70% 40%, var(--brand-blue) 0%, var(--navy) 55%, var(--navy-deep) 100%);
    display: flex;
    align-items: center;
    justify-content: center;
    gap: 34px;
  }
  .brand-mark {
    display: flex;
    align-items: center;
    gap: 18px;
  }
  .brand-dot {
    width: 54px;
    height: 54px;
    border-radius: 50%;
    background: var(--mist);
  }
  .brand-name {
    color: var(--mist);
    font-size: 64px;
    font-weight: 600;
    letter-spacing: 6px;
  }
  .brand-rule {
    width: 2px;
    height: 150px;
    background: var(--mist);
    transform: rotate(20deg);
    opacity: 0.8;
  }
  .brand-tagline {
    color: var(--mist);
    font-family: "Comfortaa", "Work Sans", sans-serif;
    font-weight: 700;
    font-size: 25px;
    line-height: 31px;
    letter-spacing: 1px;
  }
</style>
</head>
<body>
  <section class="card card-front">
    <div class="portrait" role="img" aria-label="Portrait photo of Odessa Pruitt"></div>
    <div class="divider"></div>
    <div class="identity">
      <h1 class="person-name">Odessa Pruitt, Ed.S</h1>
      <p class="person-role">Director</p>
      <ul class="contact-list">
        <li>
          <svg viewBox="0 0 14 14" aria-hidden="true"><rect x="3.5" y="0.5" width="7" height="13" rx="1.5" fill="none" stroke="#0a3d86" stroke-width="1.6"/><circle cx="7" cy="11" r="0.9" fill="#0a3d86"/></svg>
          <span>616-555-0148</span>
        </li>
        <li>
          <svg viewBox="0 0 14 14" aria-hidden="true"><path d="M3 1 L5.5 1 L6.5 4 L5 5.2 C5.8 7 7 8.2 8.8 9 L10 7.5 L13 8.5 L13 11 C13 12 12 13 11 13 C6 12.5 1.5 8 1 3 C1 2 2 1 3 1 Z" fill="#0a3d86"/></svg>
          <span>629-555-0172</span>
        </li>
        <li>
          <svg viewBox="0 0 14 14" aria-hidden="true"><rect x="1" y="3" width="12" height="8.5" rx="1" fill="none" stroke="#0a3d86" stroke-width="1.5"/><path d="M1.5 3.5 L7 8 L12.5 3.5" fill="none" stroke="#0a3d86" stroke-width="1.5"/></svg>
          <span>www.Mlgpedu.example</span>
        </li>
        <li>
          <svg viewBox="0 0 14 14" aria-hidden="true"><circle cx="7" cy="7" r="6" fill="none" stroke="#0a3d86" stroke-width="1.4"/><ellipse cx="7" cy="7" rx="2.6" ry="6" fill="none" stroke="#0a3d86" stroke-width="1.2"/><line x1="1" y1="7" x2="13" y2="7" stroke="#0a3d86" stroke-width="1.2"/></svg>
          <span>pruittodessa@mailbox.example</span>
        </li>
      </ul>
    </div>
    <div class="address-band">5073 Cormorant ridge Dr. Nashville, TN 37940</div>
  </section>

  <section class="card card-back">
    <div class="brand-mark">
      <span class="brand-dot" aria-hidden="true"></span>
      <span class="brand-name">MLGP</span>
    </div>
    <div class="brand-rule"></div>
    <p class="brand-tagline">Meadowlark<br>Learning<br>Growth<br>Partners</p>
  </section>
</body>
</html>
```